Word Template for HVAC Consultant

Looking for both a Word Template for proposals and reports (both consists of multiple pages) along with a unique "cover" or "folder" for the report (probably more of a cover since we are nearly all digital). Logo Files are uploaded. We have stationary, but not something we'd want to use on multiple pages for a report or specification book.

```html
<!DOCTYPE html>
<html lang="en">
<head>
<meta charset="utf-8">
<title>Corvane Engineering – HVAC Consultant Report Template</title>
<link href="https://fonts.googleapis.com/css2?family=Montserrat:wght@400;500;600;700;800&display=swap" rel="stylesheet">
<style>
  :root{
    --blue:#1a63a8;
    --blue-dark:#17558f;
    --orange:#f05a28;
    --text:#2b2b2b;
    --card:#ebebeb;
    --canvas:#a9a9a9;
    --white:#ffffff;
  }
  *{box-sizing:border-box;margin:0;padding:0}
  html,body{width:1200px;height:2608px;overflow:hidden}
  body{background:var(--canvas);font-family:'Montserrat',sans-serif;color:var(--text);position:relative}

  /* ---------- cover ---------- */
  .cover{position:absolute;left:320px;top:92px;width:553px;height:781px;overflow:hidden;
    background:linear-gradient(180deg,#dfe6ee 0%,#c9d4df 45%,#e4e9ef 70%);box-shadow:0 6px 18px rgba(0,0,0,.35)}
  .cover__band{position:absolute;left:0;bottom:0;width:100%;height:261px;background:var(--blue)}
  .cover__mark{position:absolute;left:236px;top:50px;width:80px;height:80px;border-radius:50%;background:var(--blue)}
  .cover__name{position:absolute;top:212px;width:100%;text-align:center;font-weight:800;font-size:40px;color:var(--orange);letter-spacing:.5px;white-space:nowrap}
  .cover__address{position:absolute;top:262px;width:100%;text-align:center;font-weight:700;font-size:15px;color:var(--blue);white-space:nowrap}
  .registration{display:flex;align-items:center;justify-content:center;gap:8px;color:var(--orange);font-weight:600;letter-spacing:3px;white-space:nowrap}
  .registration::before,.registration::after{content:"";height:2px;background:var(--orange)}
  .cover .registration{position:absolute;top:286px;width:100%;font-size:12px}
  .cover .registration::before,.cover .registration::after{width:50px}
  .cover__ring{position:absolute;left:112px;top:325px;width:330px;height:330px;border-radius:50%;background:var(--white)}
  .cover__photo{position:absolute;left:152px;top:350px;width:260px;height:280px;border-radius:50%;
    background:linear-gradient(160deg,#c7d6e4 0%,#5f8fbf 45%,#2d5f92 80%,#1f3f63 100%)}
  .cover__title{position:absolute;top:680px;width:100%;text-align:center;font-weight:800;font-size:41px;color:var(--white);letter-spacing:.5px;white-space:nowrap}
  .cover__web{position:absolute;top:735px;width:100%;text-align:center;font-weight:600;font-size:17px;color:var(--white)}

  /* ---------- inner pages ---------- */
  .page{position:absolute;width:554px;height:784px;background:var(--white);box-shadow:0 3px 10px rgba(0,0,0,.25);overflow:hidden}
  .page--toc{left:38px;top:967px}
  .page--about{left:609px;top:967px}
  .page--process{left:37px;top:1768px}
  .page--offers{left:608px;top:1770px}

  .page__footer{position:absolute;left:16px;right:0;top:737px;height:22px;display:flex;align-items:center}
  .page__web{font-size:11px;font-weight:600;color:#222;white-space:nowrap}
  .page__rule{flex:1;height:1px;background:var(--blue);margin-left:4px}
  .page__num{width:60px;height:22px;border-radius:11px 0 0 11px;background:var(--orange);color:var(--white);font-size:11px;font-weight:600;display:flex;align-items:center;justify-content:center}

  .section-title{position:absolute;left:42px;font-weight:700;font-size:23px;color:var(--blue);white-space:nowrap}
  .section-title::after{content:"";position:absolute;left:0;top:34px;width:128px;height:2px;background:var(--orange)}
  .lead{position:absolute;left:42px;width:475px;font-size:13px;line-height:15px;color:#222}

  .mini-brand{position:absolute;left:390px;top:28px;width:140px;text-align:center}
  .mini-brand__mark{width:22px;height:22px;border-radius:50%;background:var(--blue);margin:0 auto 4px}
  .mini-brand__name{font-size:8.5px;font-weight:700;color:var(--orange);white-space:nowrap}
  .mini-brand__line{font-size:5px;color:var(--blue);margin-top:1px;white-space:nowrap}

  /* table of contents */
  .toc-brand{position:absolute;top:20px;width:100%;text-align:center}
  .toc-brand__mark{width:70px;height:70px;border-radius:50%;background:var(--blue);margin:0 auto 40px}
  .toc-brand__name{font-weight:800;font-size:25px;color:var(--orange);margin-top:-2px;white-space:nowrap}
  .toc-brand__address{font-weight:700;font-size:8.5px;color:var(--blue);margin-top:1px;white-space:nowrap}
  .toc-brand .registration{font-size:7.5px;letter-spacing:2px;margin-top:1px}
  .toc-brand .registration::before,.toc-brand .registration::after{width:26px;height:1px}
  .toc-band{position:absolute;left:0;top:175px;width:112px;height:525px;background:var(--blue);border-radius:0 22px 22px 0;z-index:2}
  .toc-band__label{position:absolute;left:56px;top:262px;transform:translate(-50%,-50%) rotate(-90deg);white-space:nowrap;color:var(--white);font-weight:500;font-size:38px;letter-spacing:1px;line-height:1}
  .toc-list{position:absolute;left:0;top:207px;list-style:none;z-index:1}
  .toc-item{position:absolute;left:100px;height:36px;display:flex;align-items:center;white-space:nowrap}
  .toc-item__num{width:48px;height:36px;padding-left:14px;border-radius:0 18px 18px 0;background:var(--blue);color:var(--white);font-size:17px;font-weight:500;display:flex;align-items:center}
  .toc-item__text{margin-left:20px;font-size:14.5px;color:#222}

  /* about */
  .framed{position:absolute}
  .framed__line-top{position:absolute;left:0;top:-6px;height:2px;background:var(--orange)}
  .framed__line-bottom{position:absolute;bottom:-6px;height:2px;background:var(--orange)}
  .framed__corner-tr{position:absolute;right:-8px;top:-6px;width:28px;height:28px;border-top:6px solid var(--orange);border-right:6px solid var(--orange)}
  .framed__corner-bl{position:absolute;left:-8px;bottom:-6px;width:28px;height:28px;border-bottom:6px solid var(--orange);border-left:6px solid var(--orange)}
  .photo{position:absolute;inset:0}
  .photo--duct{background:linear-gradient(120deg,#8fa2b4 0%,#cdd6de 40%,#b9c3cc 65%,#6f88a6 100%)}

  .member{position:absolute;top:548px;width:225px}
  .member__avatar{position:absolute;left:0;top:0;width:62px;height:62px;border-radius:50%;border:3px solid var(--blue);background:linear-gradient(180deg,#f4f6f9,#dfe6ee);z-index:2}
  .member__name{position:absolute;left:40px;top:16px;width:150px;height:30px;border-radius:0 15px 15px 0;padding-left:33px;
    background:linear-gradient(90deg,#c4552d,#2a5a8c);color:var(--white);font-weight:600;font-size:17px;display:flex;align-items:center;white-space:nowrap}
  .member__bio{position:absolute;left:0;top:80px;width:220px;font-size:13px;line-height:18px;color:#222}
  .team-divider{position:absolute;left:272px;top:540px;width:1px;height:180px;background:linear-gradient(180deg,transparent,#cfcfcf,transparent)}

  /* process & offers cards */
  .card{position:absolute;width:210px;height:110px}
  .card__box{position:absolute;inset:0;background:var(--card)}
  .card__icon{position:absolute;left:50%;top:50%;transform:translate(-50%,-50%)}
  .card .framed__line-top{left:0;right:20px}
  .card .framed__line-bottom{left:20px;right:0}
  .step-heading{position:absolute;font-weight:600;font-size:18px;color:var(--blue);white-space:nowrap}
  .step-text{position:absolute;width:210px;font-size:13px;line-height:18px;color:#222}

  .photo--split{background:linear-gradient(180deg,#3c4a3a 0%,#e6e8ea 35%,#f3f4f5 70%,#4b4f4c 100%)}
  .photo--tower{background:linear-gradient(180deg,#3f7fd0 0%,#7aa9de 40%,#b6bec6 70%,#5b6f82 100%)}
  .photo--roof{background:linear-gradient(160deg,#3d8ed8 0%,#9fc5e6 35%,#8a7a6e 65%,#5e4e44 100%)}
  .photo--condenser{background:linear-gradient(180deg,#2a2e31 0%,#4a4f53 45%,#2e3236 80%,#4e6b3a 100%)}
  .price{position:absolute;width:115px;height:42px;border-radius:21px;background:linear-gradient(90deg,#c4552d,#2a5a8c);
    color:var(--white);font-weight:600;font-size:30px;display:flex;align-items:center;justify-content:center}
</style>
</head>
<body>

<!-- Cover -->
<section class="cover">
  <div class="cover__band"></div>
  <div class="cover__mark"></div>
  <h1 class="cover__name">CORVANE ENGINEERING</h1>
  <p class="cover__address">1450 ALDER RIDGE LANE, BROOKFIELD, TEXAS 75012</p>
  <p class="registration">TBPE FIRM REGISTRATION F-4172</p>
  <div class="cover__ring"></div>
  <div class="cover__photo" role="img" aria-label="Photo of an engineer in a safety vest inspecting large rooftop HVAC units under a bright sky"></div>
  <h2 class="cover__title">HVAC CONSULTANT</h2>
  <p class="cover__web">WWW.CORVANEENGINEERING.COM</p>
</section>

<!-- Page 02: Table of contents -->
<section class="page page--toc">
  <div class="toc-brand">
    <div class="toc-brand__mark"></div>
    <div class="toc-brand__name">CORVANE ENGINEERING</div>
    <div class="toc-brand__address">1450 ALDER RIDGE LANE, BROOKFIELD, TEXAS 75012</div>
    <div class="registration">TBPE FIRM REGISTRATION F-4172</div>
  </div>
  <div class="toc-band"><span class="toc-band__label">TABLE OF CONTENTS</span></div>
  <ol class="toc-list">
    <li class="toc-item" style="top:0"><span class="toc-item__num">01</span><span class="toc-item__text">Lorem ipsum dolor sit amet</span></li>
    <li class="toc-item" style="top:53px"><span class="toc-item__num">02</span><span class="toc-item__text">Lorem ipsum dolor sit amet, consectetur</span></li>
    <li class="toc-item" style="top:112px"><span class="toc-item__num">03</span><span class="toc-item__text">Lorem ipsum dolor sit amet</span></li>
    <li class="toc-item" style="top:164px"><span class="toc-item__num">04</span><span class="toc-item__text">Lorem ipsum dolor sit amet, consectetur</span></li>
    <li class="toc-item" style="top:217px"><span class="toc-item__num">05</span><span class="toc-item__text">Lorem ipsum dolor sit amet</span></li>
    <li class="toc-item" style="top:270px"><span class="toc-item__num">06</span><span class="toc-item__text">Lorem ipsum dolor sit amet, consectetur</span></li>
    <li class="toc-item" style="top:323px"><span class="toc-item__num">07</span><span class="toc-item__text">Lorem ipsum dolor sit amet</span></li>
    <li class="toc-item" style="top:376px"><span class="toc-item__num">08</span><span class="toc-item__text">Lorem ipsum dolor sit amet, consectetur</span></li>
  </ol>
  <footer class="page__footer"><span class="page__web">WWW.CORVANEENGINEERING.COM</span><span class="page__rule"></span><span class="page__num">02</span></footer>
</section>

<!-- Page 03: About us & team -->
<section class="page page--about">
  <h2 class="section-title" style="top:34px">ABOUT US</h2>
  <div class="mini-brand"><div class="mini-brand__mark"></div><div class="mini-brand__name">CORVANE ENGINEERING</div><div class="mini-brand__line">HVAC consulting services</div></div>
  <p class="lead" style="top:100px">Lorem ipsum dolor sit amet, consectetur adipiscing elit, sed do eiusmod tempor incididunt ut labore et dolore magna aliqua.</p>
  <div class="framed" style="left:44px;top:182px;width:468px;height:238px">
    <div class="photo photo--duct" role="img" aria-label="Photo of a technician in a hard hat servicing metal ductwork on a platform"></div>
    <span class="framed__line-top" style="right:60px"></span>
    <span class="framed__line-bottom" style="left:60px;right:0"></span>
    <span class="framed__corner-tr"></span>
    <span class="framed__corner-bl"></span>
  </div>
  <h2 class="section-title" style="top:450px">OUR TEAM</h2>
  <div class="team-divider"></div>
  <div class="member" style="left:42px">
    <div class="member__avatar" role="img" aria-label="Team member avatar"></div>
    <div class="member__name">JOHN DOE</div>
    <p class="member__bio">Lorem ipsum dolor sit amet, consectetur adipiscing elit, sed do eiusmod tempor incididunt ut labore et dolore magna aliqua.</p>
  </div>
  <div class="member" style="left:306px">
    <div class="member__avatar" role="img" aria-label="Team member avatar"></div>
    <div class="member__name">JANE DOE</div>
    <p class="member__bio">Lorem ipsum dolor sit amet, consectetur adipiscing elit, sed do eiusmod tempor incididunt ut labore et dolore magna aliqua.</p>
  </div>
  <footer class="page__footer"><span class="page__web">WWW.CORVANEENGINEERING.COM</span><span class="page__rule"></span><span class="page__num">03</span></footer>
</section>

<!-- Page 04: Work process -->
<section class="page page--process">
  <h2 class="section-title" style="top:24px">WORK PROCESS</h2>
  <div class="mini-brand"><div class="mini-brand__mark"></div><div class="mini-brand__name">CORVANE ENGINEERING</div><div class="mini-brand__line">HVAC consulting services</div></div>
  <p class="lead" style="top:100px">Lorem ipsum dolor sit amet, consectetur adipiscing elit, sed do eiusmod tempor incididunt ut labore et dolore magna aliqua.</p>

  <div class="card" style="left:37px;top:183px">
    <div class="card__box"></div>
    <svg class="card__icon" width="84" height="72" viewBox="0 0 84 72" fill="none" stroke="#1a63a8" stroke-width="3" stroke-linecap="round">
      <rect x="4" y="4" width="76" height="26" rx="3"/><line x1="12" y1="22" x2="72" y2="22"/>
      <path d="M20 40c-4 5 4 9 0 14s4 9 0 14"/><path d="M34 40c-4 5 4 9 0 14s4 9 0 14"/><path d="M48 40c-4 5 4 9 0 14s4 9 0 14"/><path d="M62 40c-4 5 4 9 0 14s4 9 0 14"/>
    </svg>
    <span class="framed__line-top"></span><span class="framed__line-bottom"></span><span class="framed__corner-tr"></span><span class="framed__corner-bl"></span>
  </div>
  <h3 class="step-heading" style="left:44px;top:318px">HEADING 01</h3>
  <p class="step-text" style="left:44px;top:344px">Lorem ipsum dolor sit amet, consectetur adipiscing elit, sed do eiusmod tempor</p>

  <div class="card" style="left:280px;top:183px">
    <div class="card__box"></div>
    <svg class="card__icon" width="84" height="72" viewBox="0 0 84 72" fill="none" stroke="#1a63a8" stroke-width="3" stroke-linecap="round">
      <rect x="4" y="4" width="76" height="30" rx="3"/><line x1="12" y1="12" x2="72" y2="12"/><line x1="12" y1="20" x2="72" y2="20"/>
      <circle cx="26" cy="44" r="20" fill="#ebebeb"/><line x1="26" y1="30" x2="26" y2="58"/><line x1="14" y1="37" x2="38" y2="51"/><line x1="14" y1="51" x2="38" y2="37"/>
      <path d="M54 44c-3 4 3 7 0 11s3 7 0 11"/><path d="M66 44c-3 4 3 7 0 11s3 7 0 11"/>
    </svg>
    <span class="framed__line-top"></span><span class="framed__line-bottom"></span><span class="framed__corner-tr"></span><span class="framed__corner-bl"></span>
  </div>
  <h3 class="step-heading" style="left:287px;top:318px">HEADING 02</h3>
  <p class="step-text" style="left:287px;top:344px">Lorem ipsum dolor sit amet, consectetur adipiscing elit, sed do eiusmod tempor</p>

  <div class="card" style="left:37px;top:446px">
    <div class="card__box"></div>
    <svg class="card__icon" width="70" height="76" viewBox="0 0 70 76" fill="none" stroke="#1a63a8" stroke-width="3" stroke-linecap="round">
      <rect x="6" y="4" width="58" height="14" rx="2"/><line x1="14" y1="11" x2="56" y2="11"/>
      <path d="M15 18v26M25 18v36M35 18v46M45 18v36M55 18v26"/><path d="M27 56l8 10 8-10"/><path d="M9 40l6 6 6-6M49 40l6 6 6-6"/>
    </svg>
    <span class="framed__line-top"></span><span class="framed__line-bottom"></span><span class="framed__corner-tr"></span><span class="framed__corner-bl"></span>
  </div>
  <h3 class="step-heading" style="left:44px;top:581px">HEADING 03</h3>
  <p class="step-text" style="left:44px;top:607px">Lorem ipsum dolor sit amet, consectetur adipiscing elit, sed do eiusmod tempo</p>

  <div class="card" style="left:280px;top:446px">
    <div class="card__box"></div>
    <svg class="card__icon" width="70" height="70" viewBox="0 0 70 70" fill="none" stroke="#1a63a8" stroke-width="3" stroke-linecap="round">
      <circle cx="34" cy="38" r="20"/><circle cx="34" cy="38" r="4"/><path d="M34 34c-2-8 6-12 8-6M38 40c8 2 6 10 0 8M30 40c-6 6-12 0-8-4"/>
      <path d="M12 4c-4 6-6 9-6 11a6 6 0 0 0 12 0c0-2-2-5-6-11z"/><circle cx="60" cy="60" r="5"/>
    </svg>
    <span class="framed__line-top"></span><span class="framed__line-bottom"></span><span class="framed__corner-tr"></span><span class="framed__corner-bl"></span>
  </div>
  <h3 class="step-heading" style="left:287px;top:581px">HEADING 04</h3>
  <p class="step-text" style="left:287px;top:607px">Lorem ipsum dolor sit amet, consectetur adipiscing elit, sed do eiusmod tempor</p>

  <footer class="page__footer"><span class="page__web">WWW.CORVANEENGINEERING.COM</span><span class="page__rule"></span><span class="page__num">04</span></footer>
</section>

<!-- Page 05: Offers -->
<section class="page page--offers">
  <h2 class="section-title" style="top:26px">OUR OFFERS</h2>
  <div class="mini-brand"><div class="mini-brand__mark"></div><div class="mini-brand__name">CORVANE ENGINEERING</div><div class="mini-brand__line">HVAC consulting services</div></div>
  <p class="lead" style="top:100px">Lorem ipsum dolor sit amet, consectetur adipiscing elit, sed do eiusmod tempor incididunt ut labore et dolore magna aliqua.</p>

  <div class="card" style="left:31px;top:182px">
    <div class="photo photo--split" role="img" aria-label="Photo of a row of outdoor split-system condenser units"></div>
    <span class="framed__line-top"></span><span class="framed__line-bottom"></span><span class="framed__corner-tr"></span><span class="framed__corner-bl"></span>
  </div>
  <div class="price" style="left:76px;top:314px">$100</div>

  <div class="card" style="left:274px;top:182px">
    <div class="photo photo--tower" role="img" aria-label="Photo of a rooftop cooling tower against a blue sky"></div>
    <span class="framed__line-top"></span><span class="framed__line-bottom"></span><span class="framed__corner-tr"></span><span class="framed__corner-bl"></span>
  </div>
  <div class="price" style="left:311px;top:314px">$200</div>

  <div class="card" style="left:31px;top:446px">
    <div class="photo photo--roof" role="img" aria-label="Photo of a roof-mounted ventilation unit on a tiled roof"></div>
    <span class="framed__line-top"></span><span class="framed__line-bottom"></span><span class="framed__corner-tr"></span><span class="framed__corner-bl"></span>
  </div>
  <div class="price" style="left:76px;top:578px">$100</div>

  <div class="card" style="left:274px;top:446px">
    <div class="photo photo--condenser" role="img" aria-label="Photo of two residential air-conditioner condensers beside a garden"></div>
    <span class="framed__line-top"></span><span class="framed__line-bottom"></span><span class="framed__corner-tr"></span><span class="framed__corner-bl"></span>
  </div>
  <div class="price" style="left:313px;top:578px">$200</div>

  <footer class="page__footer"><span class="page__web">WWW.CORVANEENGINEERING.COM</span><span class="page__rule"></span><span class="page__num">05</span></footer>
</section>

</body>
</html>
```